When Rivers Burn, Tivendel Book Two

We need a book cover design for a basic 9x6 trim hardcover and paperback matching the general style of our first book. Black background mainly that's visually interesting with some colorful wrap-around element that goes from the front cover, over the spine, and ends on the back. Relevant colors to the book are black, gold, green, and purple. See attached cover of book one for style. This is a medieval inspired, epic fantasy featuring thrones, sieges, and adventure. We do not want a character on the cover as the focal point.

```html
<!DOCTYPE html>
<html lang="en">
<head>
<meta charset="utf-8">
<title>When Rivers Burn — Tivendel Book Two — Cover Wrap</title>
<link rel="stylesheet" href="https://fonts.googleapis.com/css2?family=Cinzel+Decorative:wght@400;700&display=swap">
<style>
  :root {
    --space-black: #07040b;
    --deep-purple: #3a1a55;
    --violet-haze: #5b2d7e;
    --nebula-green: #1d4a34;
    --gold: #f0b43a;
    --gold-bright: #ffd46a;
    --cover-w: 1200px;
    --cover-h: 846px;
  }
  * { margin: 0; padding: 0; box-sizing: border-box; }
  html, body {
    width: var(--cover-w);
    height: var(--cover-h);
    overflow: hidden;
    background: var(--space-black);
  }
  .cover-wrap {
    position: relative;
    width: var(--cover-w);
    height: var(--cover-h);
    overflow: hidden;
    font-family: "Cinzel Decorative", "Cinzel", serif;
    color: var(--gold);
  }
  .nebula-art {
    position: absolute;
    inset: 0;
    background:
      linear-gradient(152deg, transparent 8%, rgba(240,180,58,0.28) 18%, transparent 26%, transparent 100%),
      linear-gradient(170deg, transparent 62%, rgba(240,180,58,0.22) 70%, transparent 77%),
      radial-gradient(ellipse 420px 300px at 900px 170px, rgba(110,55,150,0.75), transparent 70%),
      radial-gradient(ellipse 380px 260px at 1080px 450px, rgba(95,45,130,0.6), transparent 70%),
      radial-gradient(ellipse 300px 240px at 620px 330px, rgba(40,110,75,0.55), transparent 70%),
      radial-gradient(ellipse 240px 200px at 180px 220px, rgba(35,95,65,0.45), transparent 70%),
      radial-gradient(ellipse 380px 240px at 230px 560px, rgba(100,45,140,0.6), transparent 70%),
      radial-gradient(ellipse 260px 200px at 880px 640px, rgba(40,100,70,0.4), transparent 70%),
      var(--space-black);
  }
  .spine {
    position: absolute;
    left: 575px;
    top: 0;
    width: 50px;
    height: 100%;
  }
  .spine-volume {
    position: absolute;
    top: 128px;
    left: 0;
    width: 100%;
    text-align: center;
    font-size: 20px;
    letter-spacing: 1px;
  }
  .spine-title,
  .spine-author {
    position: absolute;
    left: 50%;
    writing-mode: vertical-rl;
    transform: translateX(-50%);
    white-space: nowrap;
    font-size: 19px;
  }
  .spine-title { top: 258px; }
  .spine-author { top: 676px; font-size: 17px; }
  .front-title {
    position: absolute;
    left: 720px;
    top: 88px;
    width: 380px;
    text-align: center;
    font-weight: 400;
    line-height: 1;
  }
  .front-title .title-line-1 {
    display: block;
    font-size: 92px;
  }
  .front-title .title-line-2 {
    display: block;
    margin-top: 26px;
    font-size: 54px;
  }
  .front-author {
    position: absolute;
    left: 740px;
    top: 684px;
    width: 310px;
    text-align: center;
    font-size: 36px;
    letter-spacing: 0.5px;
  }
</style>
</head>
<body>
  <main class="cover-wrap">
    <div class="nebula-art" role="img" aria-label="Dark starry nebula in purple and green, crossed by glowing gold lightning cracks that wrap from the back cover over the spine to the front"></div>

    <section class="spine" aria-label="Spine">
      <p class="spine-volume">II</p>
      <p class="spine-title">When Rivers Burn</p>
      <p class="spine-author">R. J. Hollis</p>
    </section>

    <section class="front-cover" aria-label="Front cover">
      <h1 class="front-title">
        <span class="title-line-1">When</span>
        <span class="title-line-2">Rivers Burn</span>
      </h1>
      <p class="front-author">R. J. Hollis</p>
    </section>
  </main>
</body>
</html>
```